Image-Folder for a bed house

We need an image folder for our company. This is intended both for private clients at trade fairs or for commercial customers during visits of our field staff, as a general idea of our company. We would therefore especially the "width" demonstrate our product range and customer animate in our showroom to come and take our service services. we would like to list the following topics (but can also be like a little shortened): our product ... * waterbeds * box springs * Mattresses and bed frames * Spa Beds & Property mattresses * gel beds / air beds * bedsteads / sofa * Seniors bed with lift * multifunction massage chair * Murphy bed / cot * bedding: blankets, pillows, bedding * furniture: storage systems, night tables, dressers, etc. exceptional service ... * Complete bedroom planning * Installation & bedroom wardrobes made to measure * sliding door systems to measure * Übersiedlungs- and assembly service * Annual waterbeds service The folder should of course be visually appealing and in the appendix you will find a large selection of images that you can use. Detailed information about us and our products can be found our website (www.posaru.at) and in the appendix to our previous image folder. We look forward to your suggestions !! Thanks in advance.

```html
<!DOCTYPE html>
<html lang="de">
<head>
<meta charset="utf-8">
<title>About us – Posaru</title>
<link rel="stylesheet" href="https://fonts.googleapis.com/css2?family=Poiret+One&family=Arimo:wght@400;700&display=swap">
<style>
  :root {
    --ink: #0d0c0e;
    --teal: #6cc1c7;
    --text: #f2f2f2;
    --photo-top: #f1efec;
    --photo-bottom: #dcd7d1;
  }
  * { margin: 0; padding: 0; box-sizing: border-box; }
  html, body { width: 1200px; height: 848px; overflow: hidden; background: var(--ink); }
  .page {
    position: relative;
    width: 1200px;
    height: 848px;
    background: var(--ink);
    font-family: "Arimo", Arial, sans-serif;
    color: var(--text);
  }
  .hero-photo {
    position: absolute;
    left: 60px; top: 14px;
    width: 567px; height: 317px;
    background: linear-gradient(180deg, var(--photo-top) 0%, var(--photo-bottom) 100%);
  }
  .page-title {
    position: absolute;
    left: 694px; top: 86px;
    font-family: "Poiret One", "Josefin Sans", sans-serif;
    font-weight: 400;
    font-size: 112px;
    line-height: 1;
    color: var(--teal);
    white-space: nowrap;
  }
  .topic {
    position: absolute;
    top: 333px;
    width: 340px;
  }
  .topic--1 { left: 60px; }
  .topic--2 { left: 430px; }
  .topic--3 { left: 801px; }
  .topic-heading {
    font-family: "Poiret One", "Josefin Sans", sans-serif;
    font-weight: 400;
    font-size: 29px;
    line-height: 38px;
    color: var(--text);
    white-space: nowrap;
  }
  .topic-number { color: var(--teal); margin-right: 7px; }
  .topic-body {
    margin-top: 18px;
    font-size: 12.8px;
    line-height: 21.2px;
    text-align: justify;
    hyphens: auto;
  }
  .topic-link {
    display: block;
    margin-top: 18px;
    text-align: right;
    font-weight: 700;
    font-size: 12.8px;
    color: var(--teal);
    text-decoration: none;
  }
  .footer-band {
    position: absolute;
    left: 0; bottom: 0;
    width: 1200px; height: 41px;
    background: var(--teal);
  }
</style>
</head>
<body>
<main class="page">
  <div class="hero-photo" role="img" aria-label="Photo of a couple lying in a bed under white bedding"></div>

  <h1 class="page-title">About us</h1>

  <section class="topic topic--1">
    <h2 class="topic-heading"><span class="topic-number">01</span>Aximili gnimetur</h2>
    <p class="topic-body">Tum faccabo rrores et eaquiat. Aximili gnimetur? Quiatet omnistrum quatur? Os alicitae nati conse pla venis si sum que plabo. Ignatemquae in nulparum eati conet quos ulpa dolest imenemp oremodi isquam quunt arcipitatur? Suntotatur am harit quam videm aut quatur, inimolores dit laborempos magnatio Gia non exped etur? Quis mod utaerumque pellorio idenimus.<br>Mintur molorrum duci cus que nobit, nonsequ amusandunt, quiaturerum, as commoditet laborat et hit qui quidit laborrunt lam, ut liquiam dolore officia vel inctur, cor res ma doluptatis ere, que conecum aut eius disquid quis dolorer ferovidendit officidi berum eturibe rspisqui temporepudi cor modis eos magnimi, ulparcipis est, quisitati cuptatu rionem eserumque pelloriequi cum apitatet ut aperiam intiandus.</p>
    <a class="topic-link" href="#">www.posaru.at</a>
  </section>

  <section class="topic topic--2">
    <h2 class="topic-heading"><span class="topic-number">02</span>Dolorer ferovidendit</h2>
    <p class="topic-body">Tum faccabo rrores et eaquiat. Aximili gnimetur? Quiatet omnistrum quatur? Os alicitae nati conse pla venis si sum que plabo. Ignatemquae in nulparum eati conet quos ulpa dolest imenemp oremodi isquam quunt arcipitatur? Suntotatur am harit quam videm aut quatur, inimolores dit laborempos magnatio Gia non exped etur? Quis mod utaerumque pellorio idenimus.<br>Mintur molorrum ducerumque pellorii cus que nobit, nonsequ amusandunt, quiaturerum, as commoditet laborat et hit qui quidit laborrunt lam, ut liquiam dolore officia vel inctur, cor res ma doluptatis ere, que conecum aut eius disquid quis dolorer ferovidendit officidi berum eturibe rspisqui temporepudi cor modis eos magnimi, ulparcipis est, quisitati cuptatu rionem esequi cum apitatet ut aperiam intiandus.</p>
    <a class="topic-link" href="#">www.posaru.at</a>
  </section>

  <section class="topic topic--3">
    <h2 class="topic-heading"><span class="topic-number">03</span>Quisitati cuptatu</h2>
    <p class="topic-body">Tum faccabo rrores et eaquiat. Aximili gnimetur? Quiatet omnistrum quatur? Os alicitae nati conse pla venis si sum que plabo. Ignatemquae in nulparum eati conet quos ulpa dolest imenemp oremodi isquam quunt arcipitatur? Suntotatur am harit quam videm aut quatur, inimolores dit laborempos magnatio Gia non exped etur? Quis mod utaerumque pellorio idenimus.<br>Mintur molorrum duci cus que nobit, nonsequ amusandunt, quiaturerum, as commoditet laborat et hit qui quidit laborrunt lam, uterumque pellori liquiam dolore officia vel inctur, cor res ma doluptatis ere, que conecum aut eius disquid quis dolorer ferovidendit officidi berum eturibe rspisqui temporepudi cor modis eos magnimi, ulparcipis est, quisitati cuptatu rionem esequi cum apitatet ut aperiam intiandus.</p>
    <a class="topic-link" href="#">www.posaru.at</a>
  </section>

  <div class="footer-band"></div>
</main>
</body>
</html>
```